H21 catalog 16-8 and 4 pages

I need 3 catalogs: one will be 16pages + one of 8 pages + one of 4 pages.
On line now, you have my draft of the catalog 16pages in power point files + original photos. (on power point files, pictures are poor quality)
The winner will have to developp 2 other catalog with design very similar to the original of 16 pages. Page 1-2-3 will be enough for me if the looking is workabe on my side. I will also need to make all this 3 catalogs for another company: only another company name changed for fist and last page. after 3 days (July 13th) and we will develop the files in the next 7 days to be ready about July 21th.
All work will be easy as soon as the first catalog is done.
Total pdf files ready for printing factory needed will be about 8 files.
If some photos are too dark, you can make correction according your idea.
The catalog is 16 A4 pages
I need 3 catalogs: 1 of 16 pages + 1 of 8 pages + 1 of 4 pages.
My draft is summarized with the 16 power point files.
You can improve the design of the background as well as the general appearance.
We don't change the police.
The positioning and layout of the photos may vary "a little" but the general logic remains the same.
An outline of your idea for the first 3 pages is sufficient so that I can designate the winner.
Once chosen, the winner will develop the 3 catalogs with identical design.
You will need a copy and paste of the 3 with a different company name.
In the end, a total of about 8 pdf files for printing "printer"
The winner will have to developp 2 other catalog with design very similar to the original of 16 pages.
To choose the winner, I do not need the full catalog ready. Page 1-2-3 will be enough for me if the looking is workabe on my side.
I will also need to make all this 3 catalogs for another company: only another company name changed for fist and last page.
I will choose the winner after 3 days (July 13th) and we will develop the files in the next 7 days to be ready about July 21th.

Target Market(s)
Professional of super market in France. Our company supply goods to supermarket in France. I need 3 catalogs: one will be 16pages + one of 8 pages + one of 4 pages. On line now, you have my draft of the catalog 16pages in power point files + original photos. (on power point files, pictures are poor quality) The winner will have to developp 2 other catalog with design very similar to the original of 16 pages. Page 1-2-3 will be enough for me if the looking is workabe on my side. I will also need to make all this 3 catalogs for another company: only another company name changed for fist and last page. after 3 days (July 13th) and we will develop the files in the next 7 days to be ready about July 21th.All work will be easy as soon as the first catalog is done.Total pdf files ready for printing factory needed will be about 8 rows. If some photos are too dark, you can make correction according your idea.The catalog is 16 pages A4 power point files. You can improve the design of the background as well as the general appearance. The font is not changed. The positioning and the layout of the photos can vary "a little" but the general logic remains the same. your idea for the first 3 pages is sufficient so that I can designate the winner. Once designated, the winner will develop the 3 catalogs with the same design. A copy and paste of the 3 with a different company name will be required. total of about 8 "printer" print pdf files I need 3 catalogs: one will be 16pages + one of 8 pages + one of 4 pages. On line now, you have my draft of the catalog 16pages in power point files + original photos. (on power point files, pictures are poor quality) The winner will have to developp 2 other catalog with design very similar to the original of 16 pages. Page 1-2-3 will be enough for me if the looking is workabe on my side. I will also need to make all this 3 catalogs for another company: only another company name changed for fist and last page. after 3 days (July 13th) and we will develop the files in the next 7 days to be ready about July 21th.All work will be easy as soon as the first catalog is done.Total pdf files ready for printing factory needed will be about 8 files.If some photos are too dark, you can make correction according to your idea.The catalog is 16 pages A4 with the 16 power point files. You can improve the design of the background as well as the general appearance. We do not change the font. The positioning and layout of the photos may vary "a little" but the general logic remains the same. An overview of your idea for the first 3 pages is sufficient so that I can designate the winner. Once designated, the winner will develop the 3 catalogs with identical design. A copy and paste of the 3 with a different company name will be required. In the end, a total of approximately 8 "printer" print pdf files
Requirements
Must have
- You are free to improve the background and the general design. The size of main photo on each A4 must remain similar as my draft.Keep the same FONTI need 3 catalogs: one will be 16pages + one of 8 pages + one of 4 pages. On line now, you have my draft of the catalog 16pages in power point files + original photos. (on power point files, pictures are poor quality) The winner will have to developp 2 other catalog with design very similar to the original of 16 pages. Page 1-2-3 will be enough for me if the looking is workabe on my side. I will also need to make all this 3 catalogs for another company: only another company name changed for fist and last page. after 3 days (July 13th) and we will develop the files in the next 7 days to be ready about July 21th.All work will be easy as soon as the first catalog is done.Total pdf files ready for printing factory needed will be about 8 rows. If some photos are too dark, you can make correction according your idea.The catalog is 16 pages A4 power point files. You can improve the design of the background as well as the general appearance. The font is not changed. The positioning and the layout of the photos can vary "a little" but the general logic remains the same. your idea for the first 3 pages is sufficient so that I can designate the winner. Once designated, the winner will develop the 3 catalogs with the same design. A copy and paste of the 3 with a different company name will be required. total of about 8 "printer" print pdf files I need 3 catalogs: one will be 16pages + one of 8 pages + one of 4 pages. On line now, you have my draft of the catalog 16pages in power point files + original photos. (on power point files, pictures are poor quality) The winner will have to developp 2 other catalog with design very similar to the original of 16 pages. Page 1-2-3 will be enough for me if the looking is workabe on my side. I will also need to make all this 3 catalogs for another company: only another company name changed for fist and last page. after 3 days (July 13th) and we will develop the files in the next 7 days to be ready about July 21th.All work will be easy as soon as the first catalog is done.Total pdf files ready for printing factory needed will be about 8 files.If some photos are too dark, you can make correction according to your idea.The catalog is 16 pages A4 with the 16 power point files. You can improve the design of the background as well as the general appearance. We do not change the font. The positioning and layout of the photos may vary "a little" but the general logic remains the same. An overview of your idea for the first 3 pages is sufficient so that I can designate the winner. Once designated, the winner will develop the 3 catalogs with identical design. A copy and paste of the 3 with a different company name will be required. In the end, a total of approximately 8 "printer" print pdf files

Nice to have
- To choose the winner, I do not need the full catalog ready. Page 1-2-3 will be enougth to see if workable or not. I need 3 catalogs: one will be 16pages + one of 8 pages + one of 4 pages. On line now, you have my draft of the catalog 16pages in power point files + original photos. (on power point files, pictures are poor quality) The winner will have to developp 2 other catalog with design very similar to the original of 16 pages. Page 1-2-3 will be enough for me if the looking is workabe on my side. I will also need to make all this 3 catalogs for another company: only another company name changed for fist and last page. after 3 days (July 13th) and we will develop the files in the next 7 days to be ready about July 21th.All work will be easy as soon as the first catalog is done.Total pdf files ready for printing factory needed will be about 8 rows. If some photos are too dark, you can make correction according your idea.The catalog is 16 pages A4 power point files. You can improve the design of the background as well as the general appearance. The font is not changed. The positioning and the layout of the photos can vary "a little" but the general logic remains the same. your idea for the first 3 pages is sufficient so that I can designate the winner. Once designated, the winner will develop the 3 catalogs with the same design. A copy and paste of the 3 with a different company name will be required. total of about 8 "printer" print pdf files I need 3 catalogs: one will be 16pages + one of 8 pages + one of 4 pages. On line now, you have my draft of the catalog 16pages in power point files + original photos. (on power point files, pictures are poor quality) The winner will have to developp 2 other catalog with design very similar to the original of 16 pages. Page 1-2-3 will be enough for me if the looking is workabe on my side. I will also need to make all this 3 catalogs for another company: only another company name changed for fist and last page. after 3 days (July 13th) and we will develop the files in the next 7 days to be ready about July 21th.All work will be easy as soon as the first catalog is done.Total pdf files ready for printing factory needed will be about 8 files.If some photos are too dark, you can make correction according to your idea.The catalog is 16 pages A4 with the 16 power point files. You can improve the design of the background as well as the general appearance. We do not change the font. The positioning and layout of the photos may vary "a little" but the general logic remains the same. An overview of your idea for the first 3 pages is sufficient so that I can designate the winner. Once designated, the winner will develop the 3 catalogs with identical design. A copy and paste of the 3 with a different company name will be required. In the end, a total of approximately 8 "printer" print pdf files

Should not have

```html
<!DOCTYPE html>
<html lang="fr">
<head>
<meta charset="utf-8">
<title>Catalogue Automne-Hiver – pages 1 à 3</title>
<link href="https://fonts.googleapis.com/css2?family=Kalam:wght@300;400;700&display=swap" rel="stylesheet">
<style>
:root{
  --orange:#e8622a;
  --ink:#1d1d1f;
  --grey-text:#6d6d72;
  --teal:#5cc4b4;
  --teal-soft:#cdeee8;
  --page-light:#eeeef2;
  --page-mid:#d6d6de;
  --page-dark:#c4c4cd;
  --white:#ffffff;
}
*{margin:0;padding:0;box-sizing:border-box}
html,body{width:1200px;height:1200px;overflow:hidden;background:var(--white)}
body{position:relative;font-family:"Kalam",cursive;color:var(--ink)}
.page{position:absolute;width:402px;height:568px;overflow:hidden;
  background:radial-gradient(ellipse at 55% 40%,var(--page-light) 0%,var(--page-mid) 55%,var(--page-dark) 100%)}
.page-cover{left:404px;top:26px}
.page-two{left:197px;top:604px}
.page-three{left:611px;top:604px}
.abs{position:absolute}
.photo{position:absolute;border-radius:6px}
.photo-family{background:linear-gradient(135deg,#b8283a 0%,#9fb3b6 45%,#1f2647 80%,#d9cfc8 100%);opacity:.85}
.photo-rack-scarf{background:linear-gradient(180deg,#c9a9a6 0%,#8a8e99 35%,#5c5f70 60%,#9b3a3f 85%,#c9a261 100%)}
.photo-rack-socks{background:linear-gradient(180deg,#e6c9c9 0%,#c8484f 30%,#e9e3e3 50%,#b7353e 75%,#efe7e2 100%)}
.photo-rack-gloves{background:linear-gradient(180deg,#dcdce4 0%,#3b3d49 30%,#c3c2c8 50%,#2b2d38 72%,#e6dede 100%)}
.photo-rack-paris{background:linear-gradient(180deg,#d8b6b7 0%,#b54a5a 22%,#3a3a44 40%,#b9a99e 52%,#2b2c36 70%,#d7a3ae 85%,#8c2233 100%)}
.photo-rack-lille{background:linear-gradient(180deg,#e9e4e4 0%,#364052 25%,#1e1f28 45%,#c27b8b 62%,#2a2a34 75%,#e3cbcb 100%)}
.photo-boxes{background:linear-gradient(150deg,#3a3037 0%,#8b3b45 40%,#2e2a33 70%,#c47d8b 100%)}

.bubble{position:absolute;background:var(--teal-soft);border:2px solid var(--teal);border-radius:4px;
  font-size:10px;line-height:1.05;text-align:center;display:flex;align-items:center;justify-content:center;padding:2px 4px}

.brand{left:32px;top:22px;display:flex;align-items:center;gap:6px}
.brand-dot{width:18px;height:18px;border-radius:50%;background:var(--orange)}
.brand-name{font-size:17px;font-weight:400;color:var(--ink)}
.season-title{left:170px;top:26px;font-size:20px;font-weight:700;color:var(--orange)}
.site-url{left:24px;top:66px;font-size:10px}
.headline{left:0;width:402px;top:80px;text-align:center;font-size:22px;font-weight:400}
.headline b{font-weight:700}
.product-title{left:160px;width:228px;top:186px;text-align:center;font-size:18px;color:var(--orange)}
.product-copy{left:160px;width:228px;top:214px;text-align:center;font-size:11px;line-height:1.35}
.product-copy .small{font-size:9.5px}

.intro-panel{left:0;top:0;width:240px;height:125px}
.intro-lead{left:0;width:220px;top:10px;text-align:center;font-size:14px;font-weight:700;line-height:1.3}
.intro-lead .big{font-size:17px}
.intro-sub{left:0;width:220px;top:52px;text-align:center;font-size:14px;color:var(--grey-text);line-height:1.35}
.intro-sub .big{font-size:18px}
.intro-note{left:0;width:220px;top:96px;text-align:center;font-size:7.5px;line-height:1.3}

.cloud{position:absolute;width:58px;height:40px}
.rack-title{position:absolute;color:var(--orange);line-height:1}
.rack-title .name{font-size:28px}
.rack-title .lead{font-size:15px}

.label{position:absolute;text-align:center;font-size:8px;line-height:1.2;font-weight:300}
.label .price{color:var(--grey-text);display:block;margin-top:3px}
.caption{position:absolute;text-align:center;font-size:9.5px;line-height:1.15}
.caption .price{color:var(--grey-text);font-size:8.5px;display:block}
.diameter{position:absolute;text-align:center;font-size:9px;line-height:1.1;width:80px}
.folio{position:absolute;top:552px;font-size:6px}
</style>
</head>
<body>

<section class="page page-cover">
  <div class="abs brand"><span class="brand-dot"></span><span class="brand-name">Teinte Lagon</span></div>
  <div class="abs season-title">Offre Automne-Hiver</div>
  <div class="abs site-url">www.teintelagon.com</div>
  <h1 class="abs headline">Reprise de <b>100%</b> de vos invendus</h1>

  <div class="photo photo-family" style="left:16px;top:118px;width:134px;height:238px" role="img" aria-label="Famille portant les sweats plaid à capuche"></div>
  <div class="bubble" style="left:182px;top:148px;width:76px;height:28px;transform:rotate(-3deg)">nouveauté !</div>

  <div class="abs product-title">le Douillo sweat plaid</div>
  <p class="abs product-copy">Le top des ventes sur les réseaux sociaux l’hiver dernier<br>Un prix public similaire aux plus grands sites mondiaux de vente en ligne<br><span class="small">Chaud, doux et de qualité (835 grammes)</span></p>

  <div class="photo photo-rack-scarf" style="left:26px;top:400px;width:64px;height:158px" role="img" aria-label="Portant d’écharpes et bonnets"></div>
  <div class="photo photo-rack-socks" style="left:170px;top:386px;width:50px;height:173px" role="img" aria-label="Portant de chaussettes fourrées"></div>
  <div class="photo photo-rack-gloves" style="left:284px;top:388px;width:56px;height:171px" role="img" aria-label="Portant de gants, bonnets et tours de cou"></div>

  <div class="bubble" style="left:75px;top:364px;width:78px;height:31px;transform:rotate(-3deg)">60 nouveaux modèles</div>
  <div class="bubble" style="left:188px;top:348px;width:80px;height:32px;transform:rotate(-3deg)">Encore plus de motifs</div>
  <div class="bubble" style="left:292px;top:338px;width:94px;height:44px;transform:rotate(-3deg)">Tous nos gants, bonnets et tours de cou</div>
</section>

<section class="page page-two">
  <svg class="abs intro-panel" viewBox="0 0 240 125" aria-hidden="true">
    <path d="M0 0 H212 L222 50 L236 56 L222 62 L218 118 Q217 122 212 122 H0 Z" fill="var(--teal-soft)" stroke="var(--teal)" stroke-width="3"/>
  </svg>
  <div class="abs intro-lead"><span class="big">3m</span> de libre dans<br>votre magasin !</div>
  <div class="abs intro-sub">Tous nos produits<br>sur ces <span class="big">3</span> portants</div>
  <div class="abs intro-note">Valorisation prix public des 3 : environ 7000€ ttc<br>Reprise de tous vos invendus</div>

  <svg class="cloud" style="left:288px;top:0" viewBox="0 0 58 40" aria-hidden="true">
    <g fill="var(--teal)"><circle cx="18" cy="20" r="14"/><circle cx="34" cy="14" r="15"/><circle cx="44" cy="24" r="12"/><circle cx="28" cy="28" r="11"/></g>
    <text x="30" y="29" text-anchor="middle" font-family="Kalam, cursive" font-size="24" fill="var(--white)">1</text>
  </svg>
  <div class="rack-title" style="left:252px;top:50px;width:120px;text-align:center"><span class="lead" style="font-size:22px">Le portant</span><br><span class="name" style="font-size:30px">Paris</span></div>

  <div class="photo photo-family" style="left:16px;top:152px;width:144px;height:168px" role="img" aria-label="Famille portant les capes poncho sweat plaid"></div>
  <div class="caption" style="left:80px;top:326px;width:96px">Cape Poncho<br>Douillo sweat Plaid<span class="price">Prix Public<br>24,90€ et 34,90€</span></div>
  <div class="photo photo-boxes" style="left:19px;top:380px;width:138px;height:185px" role="img" aria-label="Pile de boîtes du sweat plaid"></div>

  <div class="photo photo-rack-paris" style="left:179px;top:143px;width:148px;height:372px" role="img" aria-label="Portant Paris avec chaussettes, bonnets et sweats plaid"></div>
  <div class="label" style="left:330px;top:134px;width:68px">Chaussettes fourrées<span class="price">Prix Public<br>9,90€</span></div>
  <div class="label" style="left:330px;top:227px;width:68px">Tour de cou<br>Bonnets<br>Adultes &amp;<br>Enfants<span class="price">Prix Public<br>7,90€, 9,90€<br>et 15€</span></div>

  <div class="diameter" style="left:170px;top:520px">Diamètre<br>Portant: 75 cm</div>
  <div class="folio" style="left:8px">2</div>
</section>

<section class="page page-three">
  <svg class="cloud" style="left:64px;top:0" viewBox="0 0 58 40" aria-hidden="true">
    <g fill="var(--teal)"><circle cx="18" cy="20" r="14"/><circle cx="34" cy="14" r="15"/><circle cx="44" cy="24" r="12"/><circle cx="28" cy="28" r="11"/></g>
    <text x="30" y="29" text-anchor="middle" font-family="Kalam, cursive" font-size="24" fill="var(--white)">2</text>
  </svg>
  <svg class="cloud" style="left:289px;top:0" viewBox="0 0 58 40" aria-hidden="true">
    <g fill="var(--teal)"><circle cx="18" cy="20" r="14"/><circle cx="34" cy="14" r="15"/><circle cx="44" cy="24" r="12"/><circle cx="28" cy="28" r="11"/></g>
    <text x="30" y="29" text-anchor="middle" font-family="Kalam, cursive" font-size="24" fill="var(--white)">3</text>
  </svg>
  <div class="rack-title" style="left:21px;top:40px"><span class="lead">Le portant</span> <span class="name">Brest</span></div>
  <div class="rack-title" style="left:253px;top:40px"><span class="lead">Le portant</span> <span class="name">Lille</span></div>

  <div class="photo photo-rack-scarf" style="left:20px;top:93px;width:150px;height:428px" role="img" aria-label="Portant Brest garni d’écharpes et chèches"></div>
  <div class="photo photo-rack-lille" style="left:264px;top:93px;width:125px;height:425px" role="img" aria-label="Portant Lille avec chaussettes, gants et bonnets"></div>

  <div class="label" style="left:174px;top:59px;width:86px">100%<br>Echarpes Chèches<br>et Echarpes Plaid<span class="price">Prix Public:<br>7,90€ / 15€</span></div>
  <div class="label" style="left:176px;top:137px;width:84px">Tour de cou<br>Chaussettes<br>fourrées<span class="price">Prix Public: 12,90€<br>9,90€ / 15€</span></div>
  <div class="label" style="left:176px;top:240px;width:84px">Gants adultes<br>Et enfants<br>Mitaines<span class="price">Prix Public:<br>3,90€ à 5,90€</span></div>
  <div class="label" style="left:176px;top:325px;width:84px">Carrés soyeux<br>Bandeaux<br>Bonnets<br>Chaussettes<span class="price">Prix Public:<br>2,90€ / 4,90€<br>15€</span></div>
  <div class="label" style="left:174px;top:424px;width:88px">Chaussettes fourrées<br>Adultes et Enfants<span class="price">Prix Public:<br>9,90€</span></div>

  <div class="diameter" style="left:55px;top:524px">Diamètre<br>Portant: 60 cm</div>
  <div class="diameter" style="left:236px;top:524px">Diamètre<br>Portant: 50 cm</div>
  <div class="folio" style="left:390px">3</div>
</section>

</body>
</html>
```